This is an android application with the promo text:
Enter ad once, list everywhere. Now that's listing with class! TrovaMint
It is on BrindleShop now if you want to see the horrible graphics I have uploaded.
So basically there are like 5 million classified ad sites. Well I want to post on a bunch of them but I am not entering the info over and over again. TrovaMint takes care of that for you, or at least tries to help as much as it can.
Make me something cool that portrays this idea. I have the web url registered, so will need a nice website logo also for down the road.
I must have:180x120 Promo Graphic
512x512 hi res icon
1024x500 Feature graphic.
the typical android launcher icons:
72x72 png, 48x48 png, 96x96 png, 144x144 png (did I miss any?)

In addition, this project includes button making.
I have custom buttons, they are 512x512 pngs.
Each button must come with two pngs. You have to make one with state not-pressed and one with state pressed. The state-pressed should look lighted up and pushed in like a real bush button on a radio or something.
You can look at the screenshots on brindle shop for the trovamint I have already uploaded to get an idea.
I need buttons of that format that represent the following:
New Item: Entering a new Classified Add Item.
Quit: Quit the app
Manage: Managing various app settings
Search: Search for items you have already entered.
Save: Save your item.
Delete: Delete your item
List: List your item on classified ad site of your choosing
Home: Quit entering/modifying your item and go to home screen

Browser Back: go previous page in browser
Browser Forward: go next page in browser
Reload Page: reload current page
Stop: Stop loading current page

I uploaded all the bad graphics that need improved.

Please do not submit screen layouts. I do not need that. The description is very clear, I need a logo and buttons. That is it. Maybe I will try the web design board.

Reason: I am getting some good feedback so will extend,

Reason: Looks like I have one designer. Keep going you are getting better.

Radio

Enter once, list everywhere. Now that's listing with class!

```html
<!DOCTYPE html>
<html lang="en">
<head>
<meta charset="utf-8">
<title>TrovaMint – Action Buttons</title>
<link rel="stylesheet" href="https://fonts.googleapis.com/css2?family=Roboto:wght@700&display=swap">
<style>
  :root {
    --page-bg: #eeeff1;
    --band-bg: #cdd2d5;
    --button-top: #f5f5f6;
    --button-bottom: #dfe0e2;
    --icon-grey: #a3a4a6;
    --label-grey: #b3b7ba;
    --accent-red: #ef4456;
    --accent-red-dark: #dc3145;
    --white: #ffffff;
  }
  html, body {
    margin: 0;
    padding: 0;
    width: 1200px;
    height: 800px;
    overflow: hidden;
    background: var(--page-bg);
    font-family: "Roboto", sans-serif;
  }
  .canvas {
    position: relative;
    width: 1200px;
    height: 800px;
    background: var(--page-bg);
  }
  .button-band {
    position: absolute;
    left: 0;
    top: 262px;
    width: 1200px;
    height: 276px;
    background: var(--band-bg);
  }
  .button-row {
    position: absolute;
    left: 148px;
    top: 37px;
    display: flex;
    gap: 115px;
  }
  .action {
    width: 144px;
    display: flex;
    flex-direction: column;
    align-items: center;
  }
  .action-button {
    width: 144px;
    height: 144px;
    border-radius: 50%;
    background: linear-gradient(180deg, var(--button-top) 0%, var(--button-bottom) 100%);
    box-shadow:
      0 0 0 3px rgba(185, 190, 194, 0.55),
      0 5px 5px rgba(80, 86, 92, 0.35),
      0 -3px 6px rgba(255, 255, 255, 0.6),
      inset 0 -3px 3px rgba(0, 0, 0, 0.06);
    display: flex;
    align-items: center;
    justify-content: center;
  }
  .action-button svg { display: block; }
  .action-label {
    margin-top: 24px;
    font-size: 29px;
    font-weight: 700;
    line-height: 1;
    color: var(--label-grey);
    text-shadow: 0 1px 0 rgba(255, 255, 255, 0.45), 0 -1px 0 rgba(120, 125, 130, 0.25);
  }
  .action--active .action-label {
    color: var(--accent-red);
    text-shadow: 0 0 6px rgba(239, 68, 86, 0.35);
  }
</style>
</head>
<body>
<main class="canvas">
  <section class="button-band">
    <div class="button-row">
      <div class="action">
        <div class="action-button">
          <svg width="64" height="62" viewBox="0 0 64 62" aria-hidden="true">
            <polyline points="2,30 32,3 62,30" fill="none" stroke="var(--icon-grey)" stroke-width="3"/>
            <rect x="10" y="8" width="8" height="14" fill="var(--icon-grey)"/>
            <path d="M12 30 L32 12 L52 30 V60 H38 V44 H26 V60 H12 Z" fill="var(--icon-grey)"/>
          </svg>
        </div>
        <span class="action-label">Home</span>
      </div>
      <div class="action">
        <div class="action-button">
          <svg width="82" height="46" viewBox="0 0 82 46" aria-hidden="true">
            <rect x="0" y="0" width="11" height="10" fill="var(--icon-grey)"/>
            <rect x="17" y="0" width="65" height="10" fill="var(--icon-grey)"/>
            <rect x="0" y="18" width="11" height="10" fill="var(--icon-grey)"/>
            <rect x="17" y="18" width="65" height="10" fill="var(--icon-grey)"/>
            <rect x="0" y="36" width="11" height="10" fill="var(--icon-grey)"/>
            <rect x="17" y="36" width="65" height="10" fill="var(--icon-grey)"/>
          </svg>
        </div>
        <span class="action-label">Lists</span>
      </div>
      <div class="action">
        <div class="action-button">
          <svg width="64" height="64" viewBox="0 0 64 64" aria-hidden="true">
            <circle cx="32" cy="32" r="32" fill="var(--icon-grey)"/>
            <path d="M21 21 L43 43 M43 21 L21 43" stroke="var(--white)" stroke-width="2.5" stroke-linecap="round"/>
          </svg>
        </div>
        <span class="action-label">Delete</span>
      </div>
      <div class="action action--active">
        <div class="action-button">
          <svg width="64" height="64" viewBox="0 0 64 64" aria-hidden="true">
            <defs>
              <linearGradient id="save-fill" x1="0" y1="0" x2="0" y2="1">
                <stop offset="0" stop-color="var(--accent-red)"/>
                <stop offset="1" stop-color="var(--accent-red-dark)"/>
              </linearGradient>
            </defs>
            <circle cx="32" cy="32" r="32" fill="url(#save-fill)"/>
            <polyline points="20,33 28,41 45,24" fill="none" stroke="var(--white)" stroke-width="3" stroke-linecap="round" stroke-linejoin="round"/>
          </svg>
        </div>
        <span class="action-label">Save</span>
      </div>
    </div>
  </section>
</main>
</body>
</html>
```